Improve appearance of one page intro flyer

We modify and upfit medium and heavy duty trucks with equipment needed by the end user. Safety equipment, hydraulic systems, computer systems, etc. We focus on quality and customer service. We have a one page introduction page with wording only. We need graphics or whatever the designer feels would improve the appearance of the flyer and relay professionalism in the presentation.

```html
<!DOCTYPE html>
<html lang="en">
<head>
<meta charset="utf-8">
<title>Ridgeline Custom Trucks – Intro Flyer</title>
<link rel="stylesheet" href="https://fonts.googleapis.com/css2?family=Oswald:wght@400;600;700&family=Lato:wght@400;700&display=swap">
<style>
  :root {
    --navy: #2b2a7a;
    --navy-deep: #1f1e63;
    --sky: #1fa7e8;
    --sky-light: #7fd3f7;
    --red: #d8242a;
    --grey: #e3e4e6;
    --photo-top: #c3c8d0;
    --photo-bottom: #aeb2b8;
    --ink: #1d1d2b;
    --page: #f1f1f1;
    --white: #ffffff;
  }
  * { margin: 0; padding: 0; box-sizing: border-box; }
  html, body { width: 1200px; height: 601px; overflow: hidden; background: var(--page); }
  .flyer {
    position: absolute; left: 376px; top: 11px;
    width: 448px; height: 579px;
    background: var(--white);
    overflow: hidden;
    font-family: "Lato", sans-serif;
    box-shadow: 0 2px 10px rgba(0,0,0,.12);
  }
  .top-band {
    position: absolute; left: 0; top: 0; width: 448px; height: 42px;
    background: linear-gradient(90deg, #fff 45%, var(--sky-light) 80%, var(--sky) 100%);
  }
  .hero-photo {
    position: absolute; left: 0; top: 42px; width: 448px; height: 196px;
    background: linear-gradient(180deg, var(--photo-top) 0%, var(--photo-bottom) 100%);
  }
  .title-panel {
    position: absolute; left: 0; top: 0; width: 206px; height: 156px;
    background: linear-gradient(180deg, var(--navy) 70%, rgba(43,42,122,.6) 100%);
    padding: 12px 0 0 14px;
    font-family: "Oswald", sans-serif; line-height: 1;
  }
  .title-panel span { display: block; }
  .title-bold { color: var(--white); font-weight: 700; font-size: 30px; margin-bottom: 2px; }
  .title-light { color: var(--white); font-weight: 400; font-size: 30px; margin-bottom: 2px; }
  .title-panel .accent { color: var(--sky-light); }
  .brand {
    position: absolute; left: 262px; top: 26px; width: 150px;
    font-family: "Lato", sans-serif; font-weight: 700; font-size: 14px;
    color: var(--navy); text-align: center; line-height: 1.15;
  }
  .body-area {
    position: absolute; left: 0; top: 238px; width: 448px; height: 341px;
    background: linear-gradient(180deg, #fff 0%, var(--grey) 100%);
  }
  .section-tag {
    position: absolute; height: 21px; background: var(--navy);
    color: var(--white); font-family: "Oswald", sans-serif; font-weight: 600;
    font-size: 14px; line-height: 21px; padding-left: 14px;
  }
  .tag-products { left: 0; top: 254px; width: 164px; }
  .tag-partner { left: 234px; top: 254px; width: 104px; padding-left: 12px; }
  .tag-vendors { left: 234px; top: 331px; width: 104px; padding-left: 12px; }
  .services {
    position: absolute; left: 14px; top: 281px; width: 215px;
    list-style: none; font-size: 9.4px; font-weight: 700; color: var(--ink);
    line-height: 14.7px;
  }
  .services li { padding-left: 11px; position: relative; }
  .services li::before {
    content: ""; position: absolute; left: 0; top: 5px;
    width: 4px; height: 4px; border-radius: 50%; background: var(--ink);
  }
  .services li.wrap { line-height: 11px; margin: 2px 0 2px; }
  .services li.wrap::before { top: 4px; }
  .name-row { position: absolute; display: flex; align-items: center; gap: 8px; }
  .partner-row { left: 246px; top: 292px; }
  .vendor-row-1 { left: 246px; top: 366px; }
  .vendor-row-2 { left: 246px; top: 416px; }
  .org-name {
    font-family: "Oswald", sans-serif; font-weight: 600; font-size: 13px; color: var(--navy);
    width: 88px; line-height: 1.1; white-space: nowrap;
  }
  .org-name.small { font-size: 11.5px; width: 100px; }
  .org-name.red { color: var(--red); }
  .slogan {
    position: absolute; left: 246px; top: 462px; width: 196px;
    font-family: "Oswald", sans-serif; font-weight: 600; font-size: 14.5px;
    color: var(--navy); line-height: 1.05;
  }
  .note-band {
    position: absolute; left: 0; top: 516px; width: 271px; height: 44px;
    background: linear-gradient(90deg, var(--sky-light) 0%, var(--sky) 100%);
    padding: 6px 12px 0 14px;
    font-size: 8.4px; line-height: 10.6px; color: var(--navy-deep);
  }
  .contact-block {
    position: absolute; left: 271px; top: 494px; width: 177px; height: 85px;
    background: var(--navy); color: var(--white); font-style: normal;
    padding: 13px 8px 0 14px; font-size: 8.4px; line-height: 10px;
  }
  .contact-line { display: flex; gap: 5px; margin-bottom: 3px; }
  .contact-line svg { flex: none; margin-top: 1px; }
  .contact-line.phone { font-weight: 700; }
</style>
</head>
<body>
  <div class="flyer">
    <div class="top-band"></div>
    <div class="hero-photo" role="img" aria-label="Photo of a white heavy-duty tri-axle truck chassis"></div>
    <h1 class="title-panel">
      <span class="title-bold">Excellence in</span>
      <span class="title-light">Custom Truck</span>
      <span class="title-bold">Modification</span>
      <span class="title-light accent">and Upfitting</span>
    </h1>
    <div class="brand">Ridgeline<br>Custom Trucks</div>

    <div class="body-area"></div>

    <h2 class="section-tag tag-products">Products and Services</h2>
    <ul class="services">
      <li class="wrap">Hydraulic and Electric Systems for<br>the Cryogenic Industry</li>
      <li>Hydraulic All Wheel Drive</li>
      <li>Brake Retarder Systems</li>
      <li>Safety Equipment</li>
      <li>Lifting 5th Wheels</li>
      <li>Hydraulic Systems</li>
      <li>Wetline Systems</li>
      <li>PTOs</li>
      <li>Tire Pressure Monitoring</li>
      <li>Fleet Management Computer Systems</li>
      <li>Lubrication Systems - Chassis &amp; Industrial</li>
      <li>Tarping Systems</li>
      <li>Wheelbase Changes</li>
      <li>Product Pumps</li>
      <li>...And much more</li>
    </ul>

    <h2 class="section-tag tag-partner">Our Partner:</h2>
    <div class="name-row partner-row">
      <span class="org-name red" style="width:70px">Fleetway</span>
      <span class="org-name small">Work Truck Guild</span>
    </div>

    <h2 class="section-tag tag-vendors">Our Vendors:</h2>
    <div class="name-row vendor-row-1">
      <span class="org-name">Ironside</span>
      <span class="org-name red">Coverline</span>
    </div>
    <div class="name-row vendor-row-2">
      <span class="org-name">Trakmore</span>
      <span class="org-name">Veltra</span>
    </div>

    <p class="slogan">Excellent customer service<br>is the core of our business.</p>

    <p class="note-band">Ridgeline provides additional services not readily available from factory manufacturers - contact us to discuss and/or provide a quotation.</p>

    <address class="contact-block">
      <div class="contact-line phone">
        <svg width="9" height="9" viewBox="0 0 10 10"><path d="M2 1l2 2-1 1.3c.6 1.2 1.5 2.1 2.7 2.7L7 6l2 2-1.2 1.3C4.5 9 1 5.5.7 2.2z" fill="#7fd3f7"/></svg>
        <span>555-014-2290</span>
      </div>
      <div class="contact-line">
        <svg width="9" height="9" viewBox="0 0 10 10"><rect x=".5" y="2" width="9" height="6" fill="none" stroke="#7fd3f7"/><path d="M.5 2L5 5.5 9.5 2" fill="none" stroke="#7fd3f7"/></svg>
        <span>info@ridgelinetrucks.com</span>
      </div>
      <div class="contact-line">
        <svg width="9" height="10" viewBox="0 0 10 12"><path d="M5 11C2 7 1.5 5.5 1.5 4a3.5 3.5 0 017 0C8.5 5.5 8 7 5 11z" fill="#7fd3f7"/><circle cx="5" cy="4" r="1.3" fill="#2b2a7a"/></svg>
        <span>480 Harbor Commerce Way<br>- Millbrook, NC - 27000</span>
      </div>
    </address>
  </div>
</body>
</html>
```